Web design for insurance consultant. Target clients are (re)insurers, insurtech firms and vendor...

Need a crisp, modern website which will talk briefly about the firm and its principal founder. And, details around services offered for 3 different target clients: (1) re/insurance companies, (2) insurtech and IoT firms, and (3) vendors such as claims adjusting firms and home inspection firms supporting insurers

Target Market(s)

C-suite leaders of insurance companies, reinsurance companies, insurtech firms looking to innovate property insurance, and vendors selling to these insurance companies. Focus is property insurance in coastal, catastrophe-exposed regions of the US.

Coding

Coded - Design and coding required

Number of Pages Required

5+ page

Other font styles liked:
• not sure of font wanted - classic, but modern

Colors
0792cd
00a990

Requirements
Must have
• First box should use the attached "light bulb storm" picture as background.
• one change overall - remove "Get a quote" button - we do not sell to consumers, it's strictly B2B.
• For the 3 segments, use the pictures below. I could not find one I liked for "TPAs/Vendors", so welcome your suggestions.
• Want quotes in the boxes of each of the 3 market segments.
• Button on each of the 3 market segments would lead to content (not yet finished) that will explain in more detail the services to be provided to them.
Should not have
• don't want velkori plots or others showing location of business (waste of space, in my opinion)

```html
<!DOCTYPE html>
<html lang="en">
<head>
<meta charset="utf-8">
<title>Halvern Consulting</title>
<link href="https://fonts.googleapis.com/css2?family=Raleway:ital,wght@0,400;0,500;0,600;0,700;1,400&family=Open+Sans:ital,wght@0,400;0,600;0,700;1,400&family=Oswald:wght@400&display=swap" rel="stylesheet">
<style>
:root{
  --navy:#17528c;
  --navy-deep:#124678;
  --green:#6a9e1f;
  --blue:#1a8ed0;
  --ink:#1d1d1d;
  --text:#444;
  --muted:#777;
  --white:#fff;
  --footer:#232323;
  --field:#5a5a5a;
}
*{box-sizing:border-box;margin:0;padding:0}
html,body{width:1200px;height:3673px;overflow:hidden}
body{position:relative;background:var(--white);font-family:"Open Sans",sans-serif;color:var(--text)}
.abs{position:absolute}
.btn{position:absolute;display:flex;align-items:center;justify-content:center;border-radius:16px;font-family:"Raleway",sans-serif;font-weight:700;font-size:10px;letter-spacing:.5px;text-transform:uppercase;color:var(--white);background:var(--green)}
.btn--ghost{background:transparent;border:1.5px solid var(--green);color:var(--green)}
.btn--blue{background:var(--blue)}

/* header */
.site-header{position:absolute;left:0;top:0;width:1200px;height:80px;background:var(--white);z-index:3}
.brand{position:absolute;display:flex;align-items:center;gap:8px;font-family:"Raleway",sans-serif;font-weight:700;color:var(--navy)}
.brand__dot{border-radius:50%;background:var(--green)}
.site-header .brand{left:86px;top:21px;font-size:20px}
.site-header .brand__dot{width:38px;height:38px}
.nav{position:absolute;left:340px;top:31px;display:flex;font-family:"Raleway",sans-serif;font-weight:700;font-size:12px;color:var(--ink)}
.nav a{display:block;padding:0 15px;color:inherit;text-decoration:none;position:relative}
.nav a.is-active{color:var(--green)}
.nav a.is-active::before{content:"";position:absolute;left:15px;right:15px;top:-31px;height:3px;background:var(--green)}
.header-phone{position:absolute;left:833px;top:27px;display:flex;align-items:center;gap:10px;font-family:"Oswald",sans-serif;font-size:18px;color:var(--navy)}

/* hero */
.hero-art{position:absolute;left:0;top:80px}
.hero-title{position:absolute;left:0;width:1200px;top:280px;text-align:center;font-family:"Raleway",sans-serif;font-weight:600;font-size:30px;color:var(--white)}
.hero-text{position:absolute;left:400px;width:400px;top:324px;text-align:center;font-size:15px;line-height:20px;color:var(--white)}

/* about */
.about-photo{position:absolute;left:90px;top:772px;width:378px;height:378px;border-radius:50%;border:2px solid var(--navy);padding:10px}
.about-photo span{display:block;width:100%;height:100%;border-radius:50%;background:linear-gradient(135deg,#f1f3f6 0%,#c9d4df 35%,#5e7590 70%,#1f3550 100%)}
.about-rule{position:absolute;left:567px;top:772px;width:3px;height:400px;background:var(--navy)}
.about-title{position:absolute;left:649px;top:852px;font-family:"Raleway",sans-serif;font-weight:600;font-size:23px;color:var(--ink)}
.about-title em{font-style:normal;color:var(--blue)}
.about-lead{position:absolute;left:649px;top:900px;width:470px;font-size:13.5px;line-height:19px;color:#333}
.about-copy{position:absolute;left:649px;top:960px;width:470px;font-size:13px;line-height:19px;color:var(--muted)}

/* segments */
.segments-art{position:absolute;left:0;top:1250px}
.segments-title{position:absolute;left:0;width:1200px;top:1364px;text-align:center;font-family:"Raleway",sans-serif;font-weight:600;font-size:26px;line-height:32px;color:var(--white)}
.segment{position:absolute;color:var(--white)}
.segment h3{font-family:"Raleway",sans-serif;font-weight:600;font-size:19px;margin-bottom:22px}
.segment blockquote{font-family:"Raleway",sans-serif;font-weight:500;font-size:13px;line-height:20px}
.segment cite{display:block;font-style:normal;font-weight:700;font-size:12px;margin-top:14px}
.segment .btn{position:static;width:132px;height:30px;margin-top:36px}
.segment-photo{position:absolute;width:321px;height:320px;box-shadow:0 4px 14px rgba(0,0,0,.25)}

/* testimonials */
.reviews-bg{position:absolute;left:0;top:2560px;width:1200px;height:530px;background:linear-gradient(180deg,#f6f7f9,#e9edf1 55%,#f1f3f5)}
.reviews-title{position:absolute;left:0;width:1200px;top:2692px;text-align:center;font-family:"Raleway",sans-serif;font-weight:600;font-size:22px;color:var(--ink)}
.reviews-quote{position:absolute;left:305px;width:590px;top:2750px;text-align:center;font-family:"Raleway",sans-serif;font-style:italic;font-size:18px;line-height:27px;color:#888}
.reviews-quote b{font-style:normal;font-weight:700;color:#aaa;font-size:22px}
.reviewer-photo{position:absolute;left:570px;top:2896px;width:60px;height:60px;border-radius:50%;background:linear-gradient(135deg,#e2cdbd,#a27e6c)}
.reviewer-name{position:absolute;left:0;width:1200px;top:2976px;text-align:center;font-family:"Raleway",sans-serif;font-weight:700;font-size:12px;letter-spacing:1px;color:var(--navy)}
.reviewer-role{position:absolute;left:0;width:1200px;top:2996px;text-align:center;font-size:10px;letter-spacing:1px;color:var(--muted)}
.arrow{position:absolute;top:2914px;font-size:22px;color:#666}

/* footer */
.footer-art{position:absolute;left:0;top:3040px}
.site-footer .brand{left:0;width:1200px;justify-content:center;top:3160px;font-size:28px;color:var(--white)}
.site-footer .brand__dot{width:46px;height:46px}
.footer-heading{position:absolute;top:3290px;font-family:"Raleway",sans-serif;font-weight:700;font-size:14px;color:var(--white)}
.footer-phone{position:absolute;left:88px;top:3346px;font-family:"Oswald",sans-serif;font-size:24px;color:var(--white)}
.footer-small{position:absolute;left:88px;font-size:11.5px;line-height:17px;color:#bbb}
.socials{position:absolute;left:88px;top:3488px;display:flex;gap:11px}
.socials span{width:20px;height:20px;border-radius:50%;background:var(--blue)}
.quick-links{position:absolute;left:419px;top:3348px;list-style:none;font-size:12px;line-height:27px;color:#ccc}
.quick-links .is-active{color:var(--green)}
.field{position:absolute;background:var(--field);border:1px solid #777;color:#ddd;font-size:11px;padding:8px 10px}
.send{position:absolute;left:1058px;top:3491px;width:28px;height:28px;border-radius:50%;background:var(--green)}
.legal{position:absolute;top:3592px;font-size:10.5px;color:#aaa}
.legal em{font-style:normal;color:var(--green)}
</style>
</head>
<body>

<header class="site-header">
  <div class="brand"><span class="brand__dot"></span>Halvern Consulting</div>
  <nav class="nav">
    <a class="is-active">Home</a><a>About Us</a><a>Services</a><a>Testimonials</a><a>Contact Us</a>
  </nav>
  <div class="header-phone">
    <svg width="16" height="16" viewBox="0 0 24 24"><path d="M6.6 10.8a15 15 0 0 0 6.6 6.6l2.2-2.2c.3-.3.7-.4 1-.2 1.1.4 2.3.6 3.6.6.6 0 1 .4 1 1V20c0 .6-.4 1-1 1A17 17 0 0 1 3 4c0-.6.4-1 1-1h3.5c.6 0 1 .4 1 1 0 1.3.2 2.5.6 3.6.1.3 0 .7-.2 1z" fill="#17528c"/></svg>
    123-555-0178
  </div>
  <div class="btn" style="left:985px;top:24px;width:127px;height:32px">Consult Now!</div>
</header>

<svg class="hero-art" width="1200" height="620" viewBox="0 0 1200 620" role="img" aria-label="Photo of glass office towers seen from below">
  <defs>
    <linearGradient id="heroSky" x1="0" y1="0" x2="1" y2="1">
      <stop offset="0" stop-color="#a9c4e0"/><stop offset=".35" stop-color="#5e8cbd"/><stop offset=".7" stop-color="#2f609a"/><stop offset="1" stop-color="#1b4677"/>
    </linearGradient>
  </defs>
  <path d="M0 0H1200V400Q600 760 0 390Z" fill="url(#heroSky)"/>
  <path d="M0 405Q600 775 1200 415" fill="none" stroke="#17528c" stroke-width="3"/>
</svg>
<h1 class="hero-title">Consulting Services</h1>
<p class="hero-text">There are many variations of passages of Lorem Ipsum available, the majority have suffered</p>
<div class="btn btn--blue" style="left:536px;top:401px;width:128px;height:30px">Consult Now!</div>

<section>
  <div class="about-photo"><span role="img" aria-label="Photo of two consultants reviewing a tablet"></span></div>
  <div class="about-rule"></div>
  <h2 class="about-title">About the <em>Halvern</em> consulting</h2>
  <p class="about-lead">There are many variations of passages of Lorem Ipsum available, but the majority have suffered</p>
  <p class="about-copy">There are many variations of passages of Lorem Ipsum available, but the majority have suffered alteration in some form, by injected humour, or randomised words which don't look even slightly believable.</p>
  <div class="btn" style="left:654px;top:1053px;width:127px;height:30px">Discover More</div>
</section>

<div class="reviews-bg" role="img" aria-label="Faded photo of an office meeting"></div>

<svg class="segments-art" width="1200" height="1420" viewBox="0 0 1200 1420">
  <path d="M0 60Q500 -30 1200 20V70Q500 10 0 90Z" fill="#6a9e1f"/>
  <path d="M0 80Q560 0 1200 45V1340Q600 1440 0 1310Z" fill="#17528c"/>
  <path d="M1200 1330Q900 1405 480 1405Q900 1420 1200 1370Z" fill="#6a9e1f"/>
</svg>
<h2 class="segments-title">There are many variations of passages of Lorem Ipsum available,<br>but the majority have suffered</h2>

<article class="segment" style="left:88px;top:1510px;width:620px">
  <h3>(Re)Insurers</h3>
  <blockquote>"Halvern has a unique skill set in property cat that helped us refine our approach, particularly in the challenging Florida market. He was instrumental to us in distilling down our business plan, interactions and approvals with the Florida OIR, pricing and product development, and executing on our business plan.</blockquote>
  <cite>Founder and President, Insurance Company</cite>
  <div class="btn btn--ghost">Explore More</div>
</article>
<div class="segment-photo" style="left:791px;top:1464px;background:linear-gradient(135deg,#1f3a5c 0%,#dfe6ee 40%,#b3c3d4 70%,#3d4f66 100%)" role="img" aria-label="Photo of a team reviewing charts on a desk"></div>

<div class="segment-photo" style="left:88px;top:1822px;background:linear-gradient(135deg,#f2f4f7 0%,#d7dfe9 35%,#2f4f7a 60%,#e8edf3 100%)" role="img" aria-label="Photo of a business handshake over documents"></div>
<article class="segment" style="left:487px;top:1860px;width:625px">
  <h3>Insurtech / IoT</h3>
  <blockquote>"We didn't realize how hard insurance is. Alan's operational insights and suggestions across the organization (i.e., from submission/bind through to claims handling) accelerated our launch and build-out by a number of months. He was especially valuable in helping us work through operationalizing new technologies to make the process smoother, more efficient, and consumer-friendly.</blockquote>
  <cite>Founder and COO, Insurtech MGA</cite>
  <div class="btn">Explore More</div>
</article>

<article class="segment" style="left:88px;top:2234px;width:620px">
  <h3>Vendors and TPAs</h3>
  <blockquote>"Halvern knows everybody in this space. As important as his connections were to us, he also provided huge value to us in preparing and responding to RFPs. He's expensive, but worth every penny!</blockquote>
  <cite>CEO, Third Party Administrator</cite>
  <div class="btn btn--ghost">Explore More</div>
</article>
<div class="segment-photo" style="left:791px;top:2182px;background:linear-gradient(135deg,#f4f3f0 0%,#d9d4cc 35%,#4a4c55 65%,#c9b8a8 100%)" role="img" aria-label="Photo of two colleagues discussing work at a laptop"></div>

<section>
  <h2 class="reviews-title">What Our Customers Say</h2>
  <p class="reviews-quote"><b>&ldquo;</b> There are many variations of passages of Lorem Ipsum available, but the majority have suffered alteration in some form, by injected humour, or randomised words which don't look even slightly ....</p>
  <span class="arrow" style="left:464px">&lsaquo;</span>
  <span class="arrow" style="left:724px">&rsaquo;</span>
  <div class="reviewer-photo" role="img" aria-label="Customer portrait"></div>
  <p class="reviewer-name">DANIEL</p>
  <p class="reviewer-role">CONTRARY TO POPULAR</p>
</section>

<footer class="site-footer">
  <svg class="footer-art" width="1200" height="633" viewBox="0 0 1200 633">
    <path d="M0 95Q600 -35 1200 95V633H0Z" fill="#232323"/>
    <path d="M0 82Q600 -48 1200 82" fill="none" stroke="#17528c" stroke-width="3"/>
  </svg>
  <div class="brand"><span class="brand__dot"></span>Halvern Consulting</div>

  <h4 class="footer-heading" style="left:88px">Contact Us</h4>
  <p class="footer-phone">Call: +123 - 555 - 0190</p>
  <p class="footer-small" style="top:3382px">info@halvernconsulting.com</p>
  <p class="footer-small" style="top:3423px">4410 Harbor Crest Blvd Dover,<br>FL 33527</p>
  <div class="socials"><span></span><span></span><span></span><span></span></div>

  <h4 class="footer-heading" style="left:419px">Quick Links</h4>
  <ul class="quick-links">
    <li>Home</li><li class="is-active">About Us</li><li>Services</li><li>Testimonials</li><li>Blog</li><li>Contact Us</li>
  </ul>

  <h4 class="footer-heading" style="left:593px">Send Us a Message</h4>
  <div class="field" style="left:593px;top:3362px;width:166px;height:30px">Name</div>
  <div class="field" style="left:771px;top:3362px;width:164px;height:30px">Phone</div>
  <div class="field" style="left:950px;top:3362px;width:162px;height:30px">Email</div>
  <div class="field" style="left:593px;top:3402px;width:519px;height:100px">Message...</div>
  <div class="send"></div>

  <p class="legal" style="left:88px">© 2019 <em>Halvern</em> consulting. All Rights Reserved</p>
  <p class="legal" style="left:593px">Privacy Policy &nbsp; | &nbsp; Terms &amp; Conditions</p>
  <svg class="abs" style="left:1105px;top:3588px" width="18" height="16" viewBox="0 0 18 16"><path d="M2 14L9 3L16 14" fill="none" stroke="#6a9e1f" stroke-width="2"/></svg>
</footer>

</body>
</html>
```